We are looking for a clean new looking business card.

We would like a new, clean, and modern type business card with our updated contact information. We are a small a plumbing and heating and gasfitting company who offer 24 hr emergency service as well.
We feel our logo looks best on a white background.
Our current cards are outdated, both the design and the information.

Industry/Entity Type

Plumbing and heating

Contact Information for Business Card

Logo, Name, Title, Phone#, Email, Website, "24/7 Emergency Service"

Colors
0054AA
0677BA
7BADD7
CADEEF
E8F1F8

```html
<!DOCTYPE html>
<html lang="en">
<head>
<meta charset="utf-8">
<title>Clearwater Business Card</title>
<link rel="stylesheet" href="https://fonts.googleapis.com/css2?family=Open+Sans:wght@400;600;700;800&display=swap">
<style>
  :root {
    --page-bg: #e9edf1;
    --card-white: #ffffff;
    --brand-blue: #0b93c3;
    --brand-deep: #0677ba;
    --brand-navy: #0054aa;
    --ink-dark: #2f3033;
    --card-dark: #353638;
    --mark-light: #cfd2d6;
    --mark-dark: #5a5c60;
    --text-light: #ffffff;
  }
  * { box-sizing: border-box; margin: 0; padding: 0; }
  html, body { width: 1200px; height: 800px; overflow: hidden; }
  body {
    background: var(--page-bg);
    font-family: "Open Sans", Arial, sans-serif;
    position: relative;
  }
  .card {
    position: absolute;
    top: 246px;
    width: 540px;
    height: 309px;
    border-radius: 22px;
    overflow: hidden;
    box-shadow: 0 10px 30px rgba(0,0,0,0.18);
  }
  .card-front { left: 40px; background: var(--card-white); }
  .card-back { left: 620px; background: var(--card-dark); }

  .front-wave { position: absolute; inset: 0; width: 100%; height: 100%; }

  .brand {
    position: absolute;
    left: 64px;
    top: 38px;
    display: flex;
    align-items: center;
    gap: 10px;
  }
  .brand-dot {
    width: 32px; height: 32px;
    border-radius: 50%;
    background: var(--brand-deep);
  }
  .brand-name {
    font-weight: 800;
    font-size: 40px;
    letter-spacing: 0.5px;
    color: var(--brand-deep);
    line-height: 1;
  }
  .brand-services {
    position: absolute;
    left: 100px;
    top: 90px;
    font-size: 9.5px;
    font-weight: 700;
    letter-spacing: 2.5px;
    color: var(--ink-dark);
    white-space: nowrap;
  }

  .person {
    position: absolute;
    left: 30px;
    top: 258px;
    color: var(--text-light);
  }
  .person-name { font-size: 20px; font-weight: 700; letter-spacing: 0.5px; line-height: 1.1; }
  .person-title { font-size: 14px; font-weight: 400; margin-top: 1px; }

  .divider {
    position: absolute;
    left: 232px;
    top: 224px;
    width: 1px;
    height: 64px;
    background: rgba(255,255,255,0.75);
  }

  .contact {
    position: absolute;
    left: 248px;
    top: 220px;
    list-style: none;
    color: var(--text-light);
  }
  .contact li {
    display: flex;
    align-items: center;
    gap: 8px;
    font-size: 13.5px;
    line-height: 23px;
    white-space: nowrap;
  }
  .contact li:first-child { font-size: 16px; font-weight: 600; }
  .contact svg { width: 12px; height: 12px; flex: none; }

  .back-mark {
    position: absolute;
    left: 200px;
    top: 58px;
    width: 140px;
    height: 140px;
    border-radius: 50%;
    background: linear-gradient(135deg, var(--mark-light), var(--mark-dark));
  }
  .back-tagline {
    position: absolute;
    left: 0; right: 0;
    top: 232px;
    text-align: center;
    font-size: 22px;
    font-weight: 700;
    letter-spacing: 1px;
    color: var(--text-light);
  }
</style>
</head>
<body>
  <section class="card card-front">
    <svg class="front-wave" viewBox="0 0 540 309" aria-hidden="true">
      <path d="M0,250 C150,245 260,215 330,160 C390,115 460,95 540,90 L540,309 L0,309 Z" fill="var(--brand-blue)"/>
      <path d="M40,244 C170,236 260,203 318,152 C362,114 404,92 450,80 C406,98 366,120 324,158 C264,210 176,240 40,244 Z" fill="var(--ink-dark)" stroke="var(--ink-dark)" stroke-width="2"/>
    </svg>

    <div class="brand">
      <span class="brand-dot"></span>
      <span class="brand-name">clearwater</span>
    </div>
    <div class="brand-services">PLUMBING · HEATING · GASFITTING</div>

    <div class="person">
      <div class="person-name">DANIEL REYES</div>
      <div class="person-title">Founder &amp; CEO</div>
    </div>

    <div class="divider"></div>

    <ul class="contact">
      <li>
        <svg viewBox="0 0 24 24"><path fill="#fff" d="M6.6 10.8a15 15 0 0 0 6.6 6.6l2.2-2.2c.3-.3.7-.4 1-.2 1.1.4 2.3.6 3.6.6.6 0 1 .4 1 1V20c0 .6-.4 1-1 1A17 17 0 0 1 3 4c0-.6.4-1 1-1h3.5c.6 0 1 .4 1 1 0 1.3.2 2.5.6 3.6.1.3 0 .7-.2 1z"/></svg>
        (555) 214-0387
      </li>
      <li>
        <svg viewBox="0 0 24 24"><path fill="#fff" d="M2 5h20v14H2z M2 5l10 8 10-8" stroke="#0b93c3" stroke-width="1.5"/></svg>
        daniel@clearwaterpro.com
      </li>
      <li>
        <svg viewBox="0 0 24 24"><circle cx="12" cy="12" r="10" fill="#fff"/><path d="M2 12h20M12 2c3 3 3 17 0 20M12 2c-3 3-3 17 0 20" stroke="#0b93c3" stroke-width="1.5" fill="none"/></svg>
        www.clearwaterpro.com
      </li>
    </ul>
  </section>

  <section class="card card-back">
    <div class="back-mark"></div>
    <div class="back-tagline">24/7 EMERGENCY SERVICE</div>
  </section>
</body>
</html>
```